cookie box packaging sleeve design

Hi,
I'm looking to create 5 sleeves for cookies in a box.
Classic look, not too many colors. I need to be able to add the nutrition info for each sleeve at the back.
width 110 mm height 370mm

1. Salted Tahini Choc-Chip Cookie
2. Brownie White Choc Cookie
3. Peanut Butter Cookie
4. Earthquake Cookie
5.Pistachio Cookie

ideas:
Biscotti by Corvellis (https://lanto.corvellis.com.au/?welcomed)
OR
https://au.snapboardly.com/pin/4830917265504817/

Target Market(s)

Family, office and for gifts

Industry/Entity Type

Cafe/Bakery

Colors

Designer to choose colors to be used in the design.

Requirements
Should not have
• Too many colours and the photo of the cookies

```html
<!DOCTYPE html>
<html lang="en">
<head>
<meta charset="utf-8">
<title>Crumbwell House – Cookie Sleeves</title>
<link rel="stylesheet" href="https://fonts.googleapis.com/css2?family=Oswald:wght@600&family=Crimson+Text:ital@1&display=swap">
<style>
  :root {
    --page: #ffffff;
    --cream: #f2eee8;
    --frame: #f6f2ec;
    --ink: #1c1714;
    --tahini: #c6843c;
    --brownie: #3b2420;
    --peanut: #d9a96c;
    --earthquake: #d63a44;
    --pistachio: #a3c26e;
  }
  * { box-sizing: border-box; margin: 0; padding: 0; }
  html, body { width: 1200px; height: 494px; overflow: hidden; background: var(--page); }
  .sheet { position: relative; width: 1200px; height: 494px; }
  .sleeve {
    position: absolute; top: 0; width: 194px; height: 493px;
    background: var(--tone);
  }
  .sleeve--tahini { left: 36px; --tone: var(--tahini); --title: var(--tahini); }
  .sleeve--brownie { left: 270px; --tone: var(--brownie); --title: var(--brownie); }
  .sleeve--peanut { left: 504px; --tone: var(--peanut); --title: var(--peanut); }
  .sleeve--earthquake { left: 738px; --tone: var(--earthquake); --title: var(--earthquake); }
  .sleeve--pistachio { left: 972px; --tone: var(--pistachio); --title: var(--pistachio); }
  .sleeve__pattern { position: absolute; inset: 0; background: var(--tone); }
  .label {
    position: absolute; left: 25px; top: 120px; width: 145px; height: 332px;
    border: 4px solid var(--frame); border-radius: 15px; background: var(--frame);
  }
  .label__inner {
    width: 100%; height: 100%;
    border: 1.5px solid var(--tone); border-radius: 11px; background: var(--cream);
    padding-top: 38px;
  }
  .label__block {
    height: 149px; display: flex; flex-direction: column; align-items: center; text-align: center;
  }
  .brand {
    font-family: "Oswald", sans-serif; font-weight: 600; font-size: 11px;
    color: var(--ink); letter-spacing: 0.3px; line-height: 14px; height: 30px;
    display: flex; align-items: center;
  }
  .flavour {
    font-family: "Oswald", sans-serif; font-weight: 600; font-size: 16px;
    line-height: 20px; color: var(--title); margin-top: 6px; white-space: nowrap;
  }
  .description {
    font-family: "Crimson Text", serif; font-style: italic; font-size: 5.3px;
    line-height: 7px; color: var(--ink); width: 108px; margin-top: 4px;
  }
  .weight {
    font-family: "Oswald", sans-serif; font-weight: 600; font-size: 4.5px;
    color: var(--ink); margin-top: 5px; letter-spacing: 0.1px;
  }
</style>
</head>
<body>
<main class="sheet">

  <section class="sleeve sleeve--tahini">
    <div class="sleeve__pattern" role="img" aria-label="Repeating tonal lattice pattern in caramel orange"></div>
    <div class="label"><div class="label__inner">
      <div class="label__block">
        <p class="brand">Crumbwell House</p>
        <h2 class="flavour">Salted Tahini<br>Choc-Chip Cookie</h2>
        <p class="description">Golden-baked with nutty tahini, rich dark chocolate, and a hint of sea salt for the perfect sweet-salty balance</p>
        <p class="weight">250 GRAM</p>
      </div>
      <div class="label__block">
        <p class="brand">Crumbwell House</p>
        <h2 class="flavour">Salted Tahini<br>Choc-Chip Cookie</h2>
        <p class="description">Golden-baked with nutty tahini, rich dark chocolate, and a hint of sea salt for the perfect sweet-salty balance</p>
        <p class="weight">250 GRAM</p>
      </div>
    </div></div>
  </section>

  <section class="sleeve sleeve--brownie">
    <div class="sleeve__pattern" role="img" aria-label="Repeating tonal lattice pattern in dark chocolate brown"></div>
    <div class="label"><div class="label__inner">
      <div class="label__block">
        <p class="brand">Crumbwell House</p>
        <h2 class="flavour">Brownie White<br>Choc Cookie</h2>
        <p class="description">A deep, chocolatey brownie transformed into a cookie—chewy, rich, and loaded with creamy white chocolate chunks. Decadence in every bite.</p>
        <p class="weight">250 GRAM</p>
      </div>
      <div class="label__block">
        <p class="brand">Crumbwell House</p>
        <h2 class="flavour">Brownie White<br>Choc Cookie</h2>
        <p class="description">A deep, chocolatey brownie transformed into a cookie—chewy, rich, and loaded with creamy white chocolate chunks. Decadence in every bite.</p>
        <p class="weight">250 GRAM</p>
      </div>
    </div></div>
  </section>

  <section class="sleeve sleeve--peanut">
    <div class="sleeve__pattern" role="img" aria-label="Repeating tonal lattice pattern in peanut tan"></div>
    <div class="label"><div class="label__inner">
      <div class="label__block">
        <p class="brand">Crumbwell House</p>
        <h2 class="flavour">Peanut Butter<br>Cookie</h2>
        <p class="description">Thick, soft, and packed with roasted peanut butter goodness. Just the right balance of sweet and salty for that melt-in-your-mouth moment.</p>
        <p class="weight">250 GRAM</p>
      </div>
      <div class="label__block">
        <p class="brand">Crumbwell House</p>
        <h2 class="flavour">Peanut Butter<br>Cookie</h2>
        <p class="description">Thick, soft, and packed with roasted peanut butter goodness. Just the right balance of sweet and salty for that melt-in-your-mouth moment.</p>
        <p class="weight">250 GRAM</p>
      </div>
    </div></div>
  </section>

  <section class="sleeve sleeve--earthquake">
    <div class="sleeve__pattern" role="img" aria-label="Repeating tonal lattice pattern in cherry red"></div>
    <div class="label"><div class="label__inner">
      <div class="label__block">
        <p class="brand">Crumbwell House</p>
        <h2 class="flavour">Earthquake<br>Cookie</h2>
        <p class="description">A dark chocolate masterpiece with a dramatic crinkle top, crunchy outside, fudgy inside—pure chocolate indulgence.</p>
        <p class="weight">250 GRAM</p>
      </div>
      <div class="label__block">
        <p class="brand">Crumbwell House</p>
        <h2 class="flavour">Earthquake<br>Cookie</h2>
        <p class="description">A dark chocolate masterpiece with a dramatic crinkle top, crunchy outside, fudgy inside—pure chocolate indulgence.</p>
        <p class="weight">250 GRAM</p>
      </div>
    </div></div>
  </section>

  <section class="sleeve sleeve--pistachio">
    <div class="sleeve__pattern" role="img" aria-label="Repeating tonal lattice pattern in pistachio green"></div>
    <div class="label"><div class="label__inner">
      <div class="label__block">
        <p class="brand">Crumbwell House</p>
        <h2 class="flavour">Pistachio<br>Cookie</h2>
        <p class="description">Toasted pistachios meet golden-brown perfection, with a hint of vanilla and just the right chew. A cookie that feels like a treat and a treasure</p>
        <p class="weight">250 GRAM</p>
      </div>
      <div class="label__block">
        <p class="brand">Crumbwell House</p>
        <h2 class="flavour">Pistachio<br>Cookie</h2>
        <p class="description">Toasted pistachios meet golden-brown perfection, with a hint of vanilla and just the right chew. A cookie that feels like a treat and a treasure</p>
        <p class="weight">250 GRAM</p>
      </div>
    </div></div>
  </section>

</main>
</body>
</html>
```